Digital Banner for our Featured Trend- "Layered Necks"

Digital banner that features the trend & the products within them in a creative way (see the attached photos for your reference)
• Photo size: 892 X 300 pixels
• JPEG
• Including: sourcing and/ or creating key elements (prints, typography, photos)
• Establish a graphic theme, colors, background image, patterns, fonts, etc. that will amplify the trend & the products within them.
• Underneath these banners we feature the products/ style that go with this trend

Reference:
• Please reference the top banners from these pages for the type of style that we like
• http://www.brambleloft.example/the-festival-shop-trend/
• http://www.brambleloft.example/necklines/
• http://www.brambleloft.example/go-vegan/

Target Market(s)

Female: young adults

Industry/Entity Type

Digital

Number of Pages Required

1 page

Font styles to use
Decorative
Script

Requirements
Must have
• - Feature the trend name "Layered Necks" within the photo, with high fashion font & cool layout
• - Feature a few layered necklaces (please see the attache photos for your reference of the type of products we sell)
• - Sourcing and/ or creating key elements (prints, typography, photos)
• - Establish a graphic theme, colors, background image, patterns, fonts, etc. that will amplify the trend & the products within them.
Nice to have
• - Model wearing a layered necklace
• - Colorful
Should not have
• Fine Jewelry

```html
<!DOCTYPE html>
<html lang="en">
<head>
<meta charset="utf-8">
<title>Layered Necks – Trend Page</title>
<link href="https://fonts.googleapis.com/css2?family=Kaushan+Script&family=Great+Vibes&family=Pirata+One&family=Oswald:wght@500;600&family=Arimo:wght@400;700&display=swap" rel="stylesheet">
<style>
  :root{
    --page-dark:#2f2f31;
    --page-mid:#4a4a4d;
    --bar-top:#c4949a;
    --bar-bottom:#8f5c63;
    --accent-red:#c0222c;
    --white:#ffffff;
    --tab-pink:#d9bcbf;
    --tab-text:#f6ecec;
    --panel-stone:#c6bdb5;
    --panel-text:#f4efe6;
    --signup-pink:#c9a9ad;
    --help-grey:#c6c5c9;
    --cream:#f3f1cf;
    --ink:#1b1b1b;
    --caption:#ffffff;
  }
  *{box-sizing:border-box;margin:0;padding:0}
  html,body{width:1200px;height:1000px;overflow:hidden}
  body{position:relative;background:radial-gradient(circle at 60% 40%,var(--page-mid),var(--page-dark) 75%);font-family:"Arimo",sans-serif;color:var(--white)}
  .pattern-bg{position:absolute;inset:0}
  .abs{position:absolute}

  .utility-bar{left:0;top:0;width:1200px;height:40px;background:linear-gradient(var(--bar-top),var(--bar-bottom));border-bottom:1px solid #ddd}
  .utility-link{position:absolute;top:9px;font-family:"Kaushan Script",cursive;font-size:16px;color:var(--white);white-space:nowrap}
  .utility-sep{position:absolute;top:0;width:4px;height:40px;background:var(--white)}

  .main-nav a{position:absolute;top:50px;font-family:"Kaushan Script",cursive;font-size:28px;color:var(--white);text-decoration:none}
  .main-nav .sale{color:var(--accent-red)}
  .search-box{left:1027px;top:60px;width:171px;height:25px;background:linear-gradient(#9c9c9c,#6f6f6f);border:1px solid #bbb}
  .search-box span{position:absolute;left:60px;top:2px;font-family:"Arimo",sans-serif;font-weight:700;font-size:17px;color:#e6e6e6}
  .search-box svg{position:absolute;left:10px;top:3px}

  .rule-h{height:2px;background:var(--accent-red)}
  .rule-v{width:2px;background:var(--accent-red)}
  .promo{font-family:"Pirata One",cursive;font-size:20px;line-height:23px;color:var(--white);letter-spacing:.8px;white-space:nowrap}
  .promo-sep{width:4px;height:42px;background:var(--white)}

  .breadcrumb{left:11px;top:162px;font-size:19px;font-family:"Arimo",sans-serif}

  .side-panel{left:0;width:195px;height:182px}
  .side-panel svg{position:absolute;inset:0}
  .panel-title{position:absolute;left:4px;top:2px;font-family:"Great Vibes",cursive;color:var(--panel-text)}
  .panel-list{position:absolute;left:4px;list-style:none;font-family:"Oswald",sans-serif;font-weight:600;color:var(--panel-text);text-transform:uppercase}
  .panel-more{position:absolute;font-family:"Oswald",sans-serif;font-weight:500;font-size:17px;color:#111}

  .photo{position:absolute}
  .hero-title{font-family:"Great Vibes",cursive;color:var(--ink);white-space:nowrap}
  .hero-sub{font-family:"Great Vibes",cursive;color:#f3dede;-webkit-text-stroke:1px #2b2b2b;word-spacing:14px;white-space:nowrap}

  .tab{position:absolute;top:393px;height:54px}
  .tab svg{position:absolute;inset:0}
  .tab span{position:absolute;left:0;right:0;top:10px;text-align:center;font-family:"Oswald",sans-serif;font-weight:500;font-size:24px;color:var(--tab-text)}

  .product{position:absolute;top:460px;border:2px solid #111}
  .caption{position:absolute;text-align:center;font-size:15px;line-height:17px;color:var(--caption)}

  .signup-pill{left:0;top:824px;width:192px;height:112px;background:var(--signup-pink);border-radius:0 22px 22px 0}
  .help-box{left:220px;top:824px;width:232px;height:176px;background:var(--help-grey);border:2px solid #1a1a1a}
  .help-box ul{list-style:none;position:absolute;left:22px;top:14px;font-size:14.5px;line-height:18.1px;color:#fff;letter-spacing:.3px}
  .catalog-box{left:474px;top:861px;width:446px;height:114px;background:var(--cream)}
  .catalog-box p{font-family:"Oswald",sans-serif;color:var(--ink);font-size:18px;line-height:22px;position:absolute;left:27px}
  .explore{left:981px;top:857px;font-size:16px;line-height:20.5px;list-style:none;color:#f0f0f0;white-space:nowrap}
</style>
</head>
<body>
  <div class="pattern-bg" role="img" aria-label="Dark grey faceted geometric background pattern"></div>

  <header class="utility-bar abs">
    <span class="utility-link" style="left:764px">Rs. INR</span>
    <span class="utility-sep" style="left:853px"></span>
    <span class="utility-link" style="left:861px">My Account</span>
    <span class="utility-sep" style="left:946px"></span>
    <span class="utility-link" style="left:954px">Find Store</span>
    <span class="utility-sep" style="left:1036px"></span>
    <span class="utility-link" style="left:1050px">Shopping Basket</span>
  </header>

  <nav class="main-nav">
    <a style="left:190px">New</a>
    <a style="left:337px">Clothes</a>
    <a style="left:510px">Accessories</a>
    <a class="sale" style="left:740px">Sale</a>
    <a style="left:908px">Trends</a>
  </nav>
  <div class="search-box abs">
    <svg width="20" height="20" viewBox="0 0 20 20"><circle cx="11" cy="8" r="5.5" fill="none" stroke="#fff" stroke-width="2.2"/><line x1="7" y1="12" x2="2" y2="18" stroke="#fff" stroke-width="2.6"/></svg>
    <span>Search</span>
  </div>

  <div class="rule-h abs" style="left:0;top:89px;width:1200px"></div>
  <div class="promo abs" style="left:289px;top:91px">Sign Up for Emails<br>Be The First To Know!</div>
  <div class="promo-sep abs" style="left:558px;top:93px"></div>
  <div class="promo abs" style="left:569px;top:93px;font-size:18px;line-height:21px">BL Mobile App<br>Stay Connected</div>
  <div class="promo-sep abs" style="left:709px;top:93px"></div>
  <div class="promo abs" style="left:744px;top:93px">Free International Delivery<br>on ◆150◆ USD</div>
  <div class="rule-h abs" style="left:0;top:135px;width:1200px"></div>
  <div class="rule-v abs" style="left:196px;top:137px;height:863px"></div>

  <div class="breadcrumb abs">Home &gt;Trends &gt;</div>

  <section class="side-panel abs" style="top:210px">
    <svg width="195" height="182"><polygon points="0,0 120,0 195,88 120,182 0,182" fill="var(--panel-stone)" opacity=".55"/></svg>
    <div class="panel-title" style="font-size:36px">Cataloges</div>
    <ul class="panel-list" style="left:15px;top:52px;font-size:24px;line-height:33px"><li>May 15</li><li>April 15</li><li>March 15</li></ul>
    <span class="panel-more" style="left:27px;top:154px">View more</span>
  </section>

  <section class="side-panel abs" style="top:407px">
    <svg width="195" height="182"><polygon points="0,0 120,0 195,88 120,182 0,182" fill="var(--panel-stone)" opacity=".55"/></svg>
    <div class="panel-title" style="font-size:32px">LookBook</div>
    <ul class="panel-list" style="top:44px;font-size:24px;line-height:33px"><li>Bottoms Up</li><li>Peruvian Trek</li><li>Wild &amp; Free</li></ul>
    <span class="panel-more" style="left:22px;top:146px">View more</span>
  </section>

  <section class="side-panel abs" style="top:606px">
    <svg width="195" height="182"><polygon points="0,0 120,0 195,88 120,182 0,182" fill="var(--panel-stone)" opacity=".55"/></svg>
    <div class="panel-title" style="font-size:32px">Trends</div>
    <ul class="panel-list" style="top:42px;font-size:20px;line-height:27px"><li>Summer State</li><li>Vintage Loves</li><li>Santorini Sunrise</li><li>Into the City</li></ul>
    <span class="panel-more" style="left:20px;top:150px">View more</span>
  </section>

  <div class="photo" style="left:219px;top:139px;width:593px;height:254px;background:linear-gradient(100deg,#8b8f94,#c9c6c1 45%,#8f8d8a)" role="img" aria-label="Model in a grey tank top wearing layered beaded necklaces, leaning on a rock"></div>
  <div class="hero-title abs" style="left:480px;top:160px;font-size:62px">Trend</div>
  <div class="hero-sub abs" style="left:463px;top:258px;font-size:62px">Layered Necks</div>

  <div class="photo" style="left:824px;top:139px;width:376px;height:254px;background:linear-gradient(90deg,#6f5a47,#c8ab8a 50%,#bdb8b0)" role="img" aria-label="Golden girl feature: blonde model in a fur vest wearing layered gold necklaces"></div>

  <div class="rule-h abs" style="left:380px;top:420px;width:820px;height:1px"></div>
  <div class="tab" style="left:198px;width:190px"><svg width="190" height="54"><polygon points="0,4 18,27 0,50 190,54 170,27 190,0" fill="var(--tab-pink)"/></svg><span>Featured</span></div>
  <div class="tab" style="left:404px;width:190px"><svg width="190" height="54"><polygon points="0,4 18,27 0,50 190,54 170,27 190,0" fill="var(--tab-pink)"/></svg><span>Shop by color</span></div>
  <div class="tab" style="left:616px;width:192px"><svg width="192" height="54"><polygon points="0,6 18,30 0,54 192,52 172,27 192,2" fill="var(--tab-pink)"/></svg><span style="top:12px">Shop by size</span></div>

  <div class="product" style="left:218px;width:186px;height:250px;background:linear-gradient(#c9c4bd,#a89383)" role="img" aria-label="Brown lace-up leather sandals on sand"></div>
  <div class="caption" style="left:218px;top:713px;width:168px">Lace Up Sandal<br>Rs.9,461.98<br>NEW COLOR!</div>

  <div class="product" style="left:433px;width:188px;height:250px;background:linear-gradient(#e4e1dc,#3a2530 55%,#d9d5d0)" role="img" aria-label="Model in a dark floral long-sleeve mini dress"></div>
  <div class="caption" style="left:433px;top:715px;width:188px">Mid Rise<br>Rs.8,183.33</div>

  <div class="product" style="left:649px;width:237px;height:250px;background:linear-gradient(120deg,#e8dcd4,#d4b596 50%,#efe6e0)" role="img" aria-label="Close-up of layered gold pendant necklaces with coin, ring, arrow and arrowhead charms"></div>

  <div class="product" style="left:920px;width:232px;height:250px;background:radial-gradient(circle at 50% 50%,#e3c7a8 0 28%,#fbfbfb 30%)" role="img" aria-label="Nude leather wristlet pouch"></div>

  <div class="abs" style="left:968px;top:741px;font-size:15px;color:#fff;word-spacing:2px;white-space:nowrap">View All &nbsp;&nbsp;1 2 3 &nbsp;&nbsp;&nbsp;&nbsp;&nbsp;37 Styles</div>

  <div class="abs" style="left:369px;top:803px;font-size:15px;letter-spacing:.2px;white-space:nowrap">Sign Up For Our Emails! NEW FRIENDS GET FREE SHIPPING ON YOUR FIRST ORDER!</div>

  <div class="signup-pill abs">
    <div class="abs" style="left:10px;top:22px;font-family:'Kaushan Script',cursive;font-size:16px;color:#111;white-space:nowrap">Sign up for our Emails!</div>
    <div class="abs" style="left:17px;top:52px;width:140px;height:2px;background:#111"></div>
    <div class="abs" style="left:41px;top:62px;font-family:'Arimo',sans-serif;font-size:20px;color:#fff">Sign Up</div>
  </div>

  <div class="help-box abs">
    <ul>
      <li>Need Help?</li><li>ORDER STATUS</li><li>ORDERING &amp; PAYMENT</li><li>SHIPPING INFORMATION</li><li>RETURNS &amp; EXCHANGES</li><li>INTERNATIONAL ORDERS</li><li>AFFILIATES</li><li>See All Help Topics</li>
    </ul>
  </div>

  <div class="catalog-box abs">
    <p style="top:2px;font-weight:500">The May Catalog</p>
    <p style="top:24px;font-weight:600">SHOP THE CATALOG NOW</p>
    <div class="abs" style="left:28px;top:52px;width:180px;height:5px;border:1px solid #333;border-left:0;border-right:0"></div>
    <p style="top:70px;font-weight:500">Want to receive our catalogs?</p>
    <p style="top:94px;font-weight:600">SUBSCRIBE</p>
  </div>

  <div class="rule-v abs" style="left:962px;top:843px;height:142px"></div>
  <ul class="explore abs">
    <li>Explore</li><li>OUR STORY</li><li>WORK AT BRAMBLE LOFT</li><li>WHOLESALE WEBSITE</li><li>WISHLISTS</li>
  </ul>
</body>
</html>
```